International Clinical Software Company needs a new business card design

We are looking for a new business card design for our company that has recently expanded into the UK market, making us a multinational company.
After having rebranded our website and produced a new style guide, we are looking for a business card that is creative and attention grabbing, while being consistent with the style and colour scheme used on the new website, www.brookvale.example
We produce care management technology for the aged care market, but the main aspect we aim to communicate is the human element of our software, and the way it assists in providing better care for aged people, and stronger relationships between aged people and the staff that care for them.
Our current business card is a dark green with gold text, which makes the text quite difficult to read, not very aesthetically appealing and the colour scheme looks quite dated.
We would like something fresh and modern, that can still be colourful but doesn't use large blocks of dark colour, and uses the colours within our logo.
Something tying in with the leaves that are used in our logo could work quite nicely, along with the Autumn/Fall colours of soft greens, yellows and reds (also in our existing logo). However also happy to look at fresh, completely out of the box ideas we may not have yet considered.
Target Market(s)
The people that receive this business card work in the aged card or health industry and are either corporate/management level staff or clinical (Registered Nurses, care workers etc.)
Industry/Entity Type
Health Product
Contact Information for Business Card
Company Name - BrookvaleTech
Company locations: United Kingdom, Australia, New Zealand
Staff Details:
Staff name: Dermot Quill
Staff job title: Executive Chairman
Staff email: d.quill@brookvale.example
Office phone number: 01632 960418
Font styles to use
Other font styles liked:
- Calibri
Requirements
Must have
- Must include the BrookvaleTech brand name in it's current font
- Must include logo (3 leaves in gold circle)
- Must include Business Card Details
Nice to have
- Elements of gold
- White space
- Something autumn themed but not too cliched
Should not have
- No blue - used by a major competitor and we would like to differentiate from them
- Large blocks of dark green colour (the green that appears in our leaves on the logo on our current business card is the background colour and it is far too dark)

```html
<!DOCTYPE html>
<html lang="en">
<head>
<meta charset="utf-8">
<title>BrookvaleTech – Business Card</title>
<link rel="stylesheet" href="https://fonts.googleapis.com/css2?family=Carlito:ital,wght@0,400;0,700;1,700&display=swap">
<style>
  :root {
    --backdrop: #e4e5e8;
    --card: #ffffff;
    --gold: #b39a62;
    --gold-soft: #cdb98a;
    --orange: #ec8a1e;
    --brown: #4a3420;
    --grey: #6f6a63;
    --leaf-yellow: #f6d94a;
    --leaf-orange: #ee8a2a;
    --leaf-red: #d8502a;
    --leaf-green: #9aa83e;
  }
  * { box-sizing: border-box; margin: 0; padding: 0; }
  html, body {
    width: 1200px; height: 800px; overflow: hidden;
    background: var(--backdrop);
    font-family: "Carlito", "Calibri", sans-serif;
  }
  .business-card {
    position: absolute; left: 100px; top: 114px;
    width: 1000px; height: 572px;
    background: var(--card);
    box-shadow: 0 6px 22px rgba(0,0,0,0.12);
    overflow: hidden;
  }
  .leaf-artwork { position: absolute; inset: 0; width: 1000px; height: 572px; }
  .staff {
    position: absolute; left: 78px; top: 214px;
  }
  .staff-name { color: var(--orange); font-size: 34px; font-weight: 400; line-height: 1; }
  .staff-title {
    color: var(--brown); font-size: 17px; font-weight: 700;
    letter-spacing: 0.02em; text-transform: uppercase; margin-top: 4px;
  }
  .brand-mark {
    position: absolute; left: 705px; top: 142px;
    width: 96px; height: 96px; border-radius: 50%;
    border: 2px solid var(--gold); background: #fff;
  }
  .brand-name {
    position: absolute; left: 470px; top: 232px;
    color: var(--gold); font-size: 78px; font-weight: 400;
    letter-spacing: 0.01em; line-height: 1;
  }
  .locations {
    position: absolute; left: 474px; top: 326px;
    color: var(--grey); font-size: 12px; letter-spacing: 0.12em; text-transform: uppercase;
  }
  .tagline {
    position: absolute; left: 560px; top: 348px;
    color: var(--gold); font-size: 19px; font-weight: 700; font-style: italic;
  }
  .contact-list {
    position: absolute; left: 488px; top: 392px; list-style: none;
  }
  .contact-item {
    display: flex; align-items: center; gap: 12px;
    color: var(--gold); font-size: 23px; line-height: 31px;
  }
  .contact-icon { width: 18px; height: 18px; flex: none; }
</style>
</head>
<body>
  <article class="business-card">
    <svg class="leaf-artwork" viewBox="0 0 1000 572" role="img" aria-label="Scattered autumn leaves in yellow, orange, red and soft green across the top and down the right edge">
      <defs>
        <linearGradient id="leafBand" x1="0" y1="0" x2="1" y2="0.6">
          <stop offset="0" stop-color="var(--leaf-red)"/>
          <stop offset="0.25" stop-color="var(--leaf-orange)"/>
          <stop offset="0.55" stop-color="var(--leaf-yellow)"/>
          <stop offset="0.8" stop-color="var(--leaf-orange)"/>
          <stop offset="1" stop-color="var(--leaf-green)"/>
        </linearGradient>
      </defs>
      <path d="M60 30 C160 0 330 20 470 40 C620 60 760 90 880 150 C950 190 990 260 1000 330 L1000 470 C960 450 930 400 910 360 C880 300 840 250 780 220 C700 180 600 170 500 150 C380 130 260 150 170 130 C110 118 70 80 60 30 Z" fill="url(#leafBand)" opacity="0.9"/>
    </svg>

    <div class="staff">
      <h1 class="staff-name">Dermot Quill</h1>
      <p class="staff-title">Executive Chairman</p>
    </div>

    <div class="brand-mark"></div>
    <p class="brand-name">BrookvaleTech</p>
    <p class="locations">United Kingdom &nbsp;•&nbsp; New Zealand &nbsp;•&nbsp; Australia</p>
    <p class="tagline">Clinical software specialists</p>

    <ul class="contact-list">
      <li class="contact-item">
        <svg class="contact-icon" viewBox="0 0 24 24"><path d="M6.6 10.8a15 15 0 0 0 6.6 6.6l2.2-2.2a1 1 0 0 1 1-.25 11.4 11.4 0 0 0 3.6.57 1 1 0 0 1 1 1V20a1 1 0 0 1-1 1A17 17 0 0 1 3 4a1 1 0 0 1 1-1h3.5a1 1 0 0 1 1 1c0 1.25.2 2.45.57 3.57a1 1 0 0 1-.25 1z" fill="var(--orange)"/></svg>
        01632 960418
      </li>
      <li class="contact-item">
        <svg class="contact-icon" viewBox="0 0 24 24"><rect x="2" y="5" width="20" height="14" rx="1.5" fill="var(--orange)"/><path d="M3 6l9 7 9-7" stroke="#fff" stroke-width="1.6" fill="none"/></svg>
        d.quill@brookvale.example
      </li>
      <li class="contact-item">
        <svg class="contact-icon" viewBox="0 0 24 24"><circle cx="12" cy="12" r="10" fill="var(--orange)"/><path d="M2 12h20M12 2c3 3 3 17 0 20M12 2c-3 3-3 17 0 20" stroke="#fff" stroke-width="1.3" fill="none"/></svg>
        brookvale.example
      </li>
    </ul>
  </article>
</body>
</html>
```